Backbone Bright Practice Hour

I need a podcast artwork designed for me for a new podcast I am launching
Target Market(s)
Chiropractors
Industry/Entity Type
Chiropractor
Requirements
Must have
- This image and the title of the show

```html
<!DOCTYPE html>
<html lang="en">
<head>
<meta charset="utf-8">
<title>Backbone Bright Practice Hour – Podcast Artwork</title>
<link rel="stylesheet" href="https://fonts.googleapis.com/css2?family=Anton&family=Oswald:wght@700&family=Yellowtail&display=swap">
<style>
  :root {
    --page-bg: #ffffff;
    --wall-warm: #c98a5a;
    --wall-light: #e8c9a2;
    --door-amber: #d9a24a;
    --glass-dark: #3a2a24;
    --panel-blue: #5fb0d8;
    --panel-blue-deep: #2f6f9e;
    --title-red: #d4231c;
    --title-red-dark: #7a0e0a;
    --title-white: #ffffff;
    --title-ice: #cfe9f7;
    --title-orange: #f39a1c;
    --title-yellow: #ffe15a;
    --ink-dark: #1d1a22;
    --sign-green: #1f3a2e;
    --mic-silver: #d9dde2;
    --mic-shadow: #5a5f66;
  }
  * { box-sizing: border-box; margin: 0; padding: 0; }
  html, body { width: 1200px; height: 758px; overflow: hidden; background: var(--page-bg); }
  .canvas { position: relative; width: 1200px; height: 758px; }

  .cover {
    position: absolute; width: 711px; height: 711px; overflow: hidden;
    transform-origin: top left;
  }
  .cover--large { left: 23px; top: 23px; }
  .cover--medium { left: 776px; top: 58px; transform: scale(0.566); }
  .cover--small { left: 875px; top: 478px; transform: scale(0.286); }

  .scene-photo {
    position: absolute; inset: 0;
    background:
      linear-gradient(90deg, transparent 0 73%, rgba(0,0,0,0) 73%),
      linear-gradient(90deg, var(--glass-dark) 0 14%, var(--wall-light) 14% 18%, var(--glass-dark) 18% 40%, var(--door-amber) 40% 62%, var(--wall-light) 62% 70%, var(--wall-warm) 70% 100%);
  }
  .scene-photo::after {
    content: ""; position: absolute; right: 0; top: 0; width: 30%; height: 100%;
    background: repeating-linear-gradient(180deg, #d7a67a 0 10px, #a86d48 10px 14px, #e2bd95 14px 22px);
    opacity: .85;
  }
  .blue-panel {
    position: absolute; inset: 0;
    background: radial-gradient(circle at 35% 70%, var(--panel-blue) 0%, var(--panel-blue-deep) 90%);
    clip-path: polygon(0 18%, 58% 60%, 62% 100%, 0 100%);
  }
  .mic {
    position: absolute; left: 420px; top: 320px; width: 230px; height: 520px;
    border-radius: 115px 115px 30px 30px;
    background: linear-gradient(90deg, var(--mic-shadow), var(--mic-silver) 40%, #fff 55%, var(--mic-shadow));
    transform: rotate(-38deg);
  }

  .sign {
    position: absolute; right: 28px; top: 18px; width: 160px; height: 130px;
    background: var(--sign-green); border: 4px solid #e9eef0; border-radius: 18px 18px 40px 40px;
    display: flex; align-items: flex-end; justify-content: center; padding-bottom: 34px;
    color: #fff; font: 700 19px "Oswald", sans-serif; letter-spacing: .5px;
  }
  .brand {
    position: absolute; left: 100px; top: 14px;
    display: flex; align-items: center; gap: 8px;
    font: 700 18px "Oswald", sans-serif; color: #1b3f8c;
    background: #e9eef6; border-radius: 20px; padding: 6px 16px;
  }
  .brand-dot { width: 12px; height: 12px; border-radius: 50%; background: #1b3f8c; }
  .badge { position: absolute; left: 120px; top: 64px; width: 96px; height: 36px; border-radius: 18px; background: #c7a65a; }

  .title { position: absolute; left: 26px; top: 96px; width: 440px; }
  .title-the {
    font: 400 92px/1 "Yellowtail", cursive; color: var(--title-white);
    text-shadow: 3px 4px 0 var(--title-red-dark);
  }
  .title-line {
    display: block; font-family: "Anton", sans-serif; line-height: .95; transform: scaleY(1.15); transform-origin: left top;
  }
  .title-backbone {
    margin-top: 6px; font-size: 94px; color: var(--title-red);
    text-shadow: 3px 4px 0 var(--title-red-dark), 0 0 0 #fff;
  }
  .title-bright {
    margin-top: 18px; font-size: 112px; color: var(--title-ice);
    text-shadow: 3px 4px 0 var(--panel-blue-deep);
  }
  .title-practice {
    margin-top: 22px; font-size: 72px;
    background: linear-gradient(180deg, var(--title-yellow), var(--title-orange) 50%, var(--title-red));
    -webkit-background-clip: text; background-clip: text; color: transparent;
    filter: drop-shadow(3px 3px 0 var(--title-red-dark));
    transform: scaleY(1.15) rotate(-4deg);
  }
  .title-hour {
    margin: 4px 0 0 60px; font: 400 100px/1 "Yellowtail", cursive; color: var(--title-white);
    text-shadow: 3px 4px 0 var(--title-red-dark);
  }
  .host-with {
    position: absolute; left: 140px; top: 630px;
    font: 400 40px/1 "Yellowtail", cursive; color: var(--title-white); text-shadow: 2px 3px 0 var(--ink-dark);
  }
  .host-name {
    position: absolute; left: 38px; top: 668px;
    font: 700 40px/1 "Oswald", sans-serif; color: var(--title-white); letter-spacing: .5px;
    text-shadow: 2px 3px 0 var(--ink-dark);
  }
</style>
</head>
<body>
<div class="canvas">
  <section class="cover cover--large">
    <div class="scene-photo" role="img" aria-label="Photo of a chiropractic clinic entrance with glass doors and stone wall"></div>
    <div class="blue-panel" role="img" aria-label="Textured blue backdrop"></div>
    <div class="mic" role="img" aria-label="Vintage studio microphone"></div>
    <div class="brand"><span class="brand-dot"></span>Align-Well</div>
    <div class="badge"></div>
    <div class="sign">Chiropractor</div>
    <h1 class="title">
      <span class="title-the">The</span>
      <span class="title-line title-backbone">BACKBONE</span>
      <span class="title-line title-bright">BRIGHT</span>
      <span class="title-line title-practice">PRACTICE</span>
      <span class="title-hour">Hour</span>
    </h1>
    <div class="host-with">With</div>
    <div class="host-name">DR. NOLAN REEVES</div>
  </section>

  <section class="cover cover--medium">
    <div class="scene-photo" role="img" aria-label="Photo of a chiropractic clinic entrance with glass doors and stone wall"></div>
    <div class="blue-panel" role="img" aria-label="Textured blue backdrop"></div>
    <div class="mic" role="img" aria-label="Vintage studio microphone"></div>
    <div class="brand"><span class="brand-dot"></span>Align-Well</div>
    <div class="badge"></div>
    <div class="sign">Chiropractor</div>
    <div class="title">
      <span class="title-the">The</span>
      <span class="title-line title-backbone">BACKBONE</span>
      <span class="title-line title-bright">BRIGHT</span>
      <span class="title-line title-practice">PRACTICE</span>
      <span class="title-hour">Hour</span>
    </div>
    <div class="host-with">With</div>
    <div class="host-name">DR. NOLAN REEVES</div>
  </section>

  <section class="cover cover--small">
    <div class="scene-photo" role="img" aria-label="Photo of a chiropractic clinic entrance with glass doors and stone wall"></div>
    <div class="blue-panel" role="img" aria-label="Textured blue backdrop"></div>
    <div class="mic" role="img" aria-label="Vintage studio microphone"></div>
    <div class="brand"><span class="brand-dot"></span>Align-Well</div>
    <div class="badge"></div>
    <div class="sign">Chiropractor</div>
    <div class="title">
      <span class="title-the">The</span>
      <span class="title-line title-backbone">BACKBONE</span>
      <span class="title-line title-bright">BRIGHT</span>
      <span class="title-line title-practice">PRACTICE</span>
      <span class="title-hour">Hour</span>
    </div>
    <div class="host-with">With</div>
    <div class="host-name">DR. NOLAN REEVES</div>
  </section>
</div>
</body>
</html>
```